Business Card Design Project

We need a simple business card design that uses our current logo.
We need to have the current logo put into a high res format.
We need to have 1 card made with contact information.
We will supply the information for the 4 employees.
Industry/Entity Type
Business
Requirements
Must have
- The contact information is as follows:
Mark Dellweather
Producer/CEO
c. 949-555-0147
f. 650-555-0193
markd@lanternbay.example
Al Vostrand, CFO
c. 949-555-0162
f. 650-555-0193
alv@lanternbay.example
Peter Malvane, PR
c. 267-555-0128
f. 650-555-0193
pmalvane@lanternbay.example
Tim Garrowby, Producer
c. 949-555-0184
f. 650-555-0193
timg@lanternbay.example
The address for all cards is:
318 W Calle Norvento #2715, San Clemente, CA 92681

```html
<!DOCTYPE html>
<html lang="en">
<head>
<meta charset="UTF-8">
<title>Lantern Bay Media – Business Cards</title>
<link rel="stylesheet" href="https://fonts.googleapis.com/css2?family=Open+Sans:wght@400;600;800&display=swap">
<style>
  :root {
    --backdrop: #6f6f6f;
    --card-paper: #f4f4f2;
    --ink: #1c1c1c;
    --brand-blue: #3a8fc9;
    --card-shadow: rgba(0, 0, 0, 0.35);
  }
  * { box-sizing: border-box; margin: 0; padding: 0; }
  html, body {
    width: 1200px;
    height: 922px;
    overflow: hidden;
  }
  body {
    background: var(--backdrop);
    font-family: "Open Sans", Arial, sans-serif;
    color: var(--ink);
    display: flex;
    flex-direction: column;
    align-items: center;
    justify-content: center;
    gap: 64px;
  }
  .card {
    position: relative;
    width: 620px;
    height: 354px;
    background: var(--card-paper);
    box-shadow: 0 8px 22px var(--card-shadow);
  }
  .brand-name {
    font-weight: 800;
    color: var(--brand-blue);
    text-transform: uppercase;
    letter-spacing: 0.5px;
    font-size: 34px;
    line-height: 1;
    white-space: nowrap;
  }
  .person-name {
    font-weight: 400;
    font-size: 31px;
    line-height: 1.1;
  }
  .person-title {
    font-size: 13px;
    line-height: 1.3;
  }
  .contact {
    font-size: 16px;
    line-height: 1.4;
  }

  /* Layout A: name top right, brand left, contact bottom right */
  .card--split .brand-name {
    position: absolute;
    left: 40px;
    top: 104px;
  }
  .card--split .identity {
    position: absolute;
    right: 38px;
    top: 48px;
    text-align: right;
  }
  .card--split .contact {
    position: absolute;
    right: 38px;
    bottom: 40px;
    text-align: right;
  }

  /* Layout B: centered stack */
  .card--centered {
    display: flex;
    flex-direction: column;
    align-items: center;
    text-align: center;
  }
  .card--centered .brand-name { margin-top: 64px; }
  .card--centered .identity { margin-top: 42px; }
  .card--centered .contact {
    position: absolute;
    left: 0;
    right: 0;
    bottom: 38px;
    font-size: 15px;
  }
</style>
</head>
<body>
  <section class="card card--split" aria-label="Business card, split layout">
    <div class="brand-name">Lantern Bay Media</div>
    <div class="identity">
      <p class="person-name">Mark Dellweather</p>
      <p class="person-title">Producer/CEO</p>
    </div>
    <div class="contact">
      <p>c. 949-555-0147</p>
      <p>f. 650-555-0193</p>
      <p>markd@lanternbay.example</p>
    </div>
  </section>

  <section class="card card--centered" aria-label="Business card, centered layout">
    <div class="brand-name">Lantern Bay Media</div>
    <div class="identity">
      <p class="person-name">Mark Dellweather</p>
      <p class="person-title">Producer/CEO</p>
    </div>
    <p class="contact">c. 949-555-0147 • f. 650-555-0193 • markd@lanternbay.example</p>
  </section>
</body>
</html>
```